Wine label for family vineyard start-up

Brand new family vineyard needs a new label:

The information we need on the label is the following:
- Merlot & Cabernet (variety)
- Serra Valderina (location)
- 2016 (vintage)

The style of the label should be graphic / minimal / masculine.

This is a wine made by three 35yr old guys

Target Market(s)

young & urban

Industry/Entity Type

Vineyard

Logo Text

Merlot & Cabernet / Serra Valderina / 2016

Font styles to use
Sans Serif

Requirements
Must have
• clearly legible
• aesthetically pleasing [minimalist]
• sans serif

```html
<!DOCTYPE html>
<html lang="en">
<head>
<meta charset="utf-8">
<title>Serra Valderina 2016 – Wine Label</title>
<link href="https://fonts.googleapis.com/css2?family=Patrick+Hand&display=swap" rel="stylesheet">
<style>
  :root {
    --wine-center: #7a2024;
    --wine-edge: #561f25;
    --label-cream: #fefbe0;
    --ink: #1c1a17;
    --stain-tone: #f2ecce;
  }
  html, body {
    margin: 0;
    padding: 0;
    width: 1200px;
    height: 1200px;
    overflow: hidden;
  }
  .canvas {
    position: relative;
    width: 1200px;
    height: 1200px;
    background: radial-gradient(circle at 50% 50%, var(--wine-center) 0%, var(--wine-edge) 100%);
  }
  .label {
    position: absolute;
    left: 400px;
    top: 282px;
    width: 374px;
    height: 638px;
    background: var(--label-cream);
    color: var(--ink);
    font-family: "Patrick Hand", sans-serif;
  }
  .stain-mark {
    position: absolute;
    left: 84px;
    top: 64px;
    width: 206px;
    height: 266px;
    border-radius: 50%;
    background: var(--stain-tone);
  }
  .label-text {
    position: absolute;
    left: 0;
    width: 100%;
    margin: 0;
    text-align: center;
    line-height: 1;
    font-weight: 400;
  }
  .variety {
    top: 373px;
    font-size: 40px;
    letter-spacing: 1px;
  }
  .place-name {
    top: 403px;
    font-size: 106px;
    letter-spacing: 2px;
  }
  .place-area {
    top: 510px;
    font-size: 62px;
    letter-spacing: 1px;
  }
  .vintage {
    top: 581px;
    font-size: 32px;
    letter-spacing: 1px;
  }
</style>
</head>
<body>
  <main class="canvas">
    <section class="label">
      <div class="stain-mark" role="img" aria-label="Two overlapping wine-glass ring stains drawn in dark ink"></div>
      <p class="label-text variety">Merlot Cabarnet</p>
      <h1 class="label-text place-name">SERRA</h1>
      <p class="label-text place-area">VALDERINA</p>
      <p class="label-text vintage">2016</p>
    </section>
  </main>
</body>
</html>
```